The Larkspur Bay Clinic Flyer Design

The Larkspur Bay Clinic is a new company providing Dietetic services for people with gastrointestinal disorders. The main client base would be people suffering from Irritable Bowel Syndrome. IBS is a collection of symptoms which (will be individual to the suffer) including constipation/diarrhoea/abdominal pain or discomfort/bloating/belching/flatulence/stomach gurgling/reflux/nausea/urgency/incomplete emptying/fatigue/headaches. IBS affects approx 30% of the population. Previous treatments have generally been ineffectual and include medication, hypnotherapy, healthy eating.
Recently it has been found that the FODMAP diet (a diet low in fermentable Carbohydrates) has been effective in 75% of sufferers.
The Low FODMAP diet is complex and it is highly recommended that it is undertaken only under the supervision of a suitably qualified dietitian. Treatment is available within the QWR but is usually accessible only following consultation with a Gastroenterologist. Most GP's have never heard of this treatment as the research was only published in 2009 in Australia and is yet to filter through to the general practitioner. The Larkspur Bay Clinic is the only clinic in the UK offering dietetic lead specialist services.
I am a member of the KSL and RWMT (logos provided)
The flyer would be double sided, informing the patient of all the self help steps they could take if they have IBS then recommending that they contact The Larkspur Bay Clinic for specialist advice.
Self Help: Healthy eating, regular meals, good intake of non caffeinated non alcoholic non fizzy drinks, regular exercise, stress management.
The flyer would be left in GP surgeries, Health centres, holistic therapy centres, or through doors.
Majority female aged 20-50, able to pay for private services
Clinic

```html
<!DOCTYPE html>
<html lang="en">
<head>
<meta charset="utf-8">
<title>The Larkspur Bay Clinic Flyer</title>
<link rel="stylesheet" href="https://fonts.googleapis.com/css2?family=Noto+Serif:wght@400;700&display=swap">
<style>
  :root {
    --backdrop: #1f1f1f;
    --paper: #ffffff;
    --cyan: #16b1e0;
    --navy: #1b4a86;
    --ink: #4a4a4a;
    --rule: #cfcfcf;
  }
  * { box-sizing: border-box; margin: 0; padding: 0; }
  html, body { width: 1200px; height: 1000px; overflow: hidden; }
  body { background: var(--backdrop); font-family: "Noto Serif", Georgia, serif; }

  .flyer-page {
    position: absolute; left: 275px; width: 650px; height: 460px;
    background: var(--paper); overflow: hidden;
  }
  .flyer-page--front { top: 35px; }
  .flyer-page--back { top: 505px; }

  .page-shapes, .page-illustration { position: absolute; left: 0; top: 0; }

  .clinic-title {
    position: absolute; left: 38px; top: 40px; color: var(--paper);
    line-height: 1; text-shadow: 0 2px 3px rgba(0,0,0,.18);
  }
  .clinic-title__top { display: block; font-size: 36px; font-weight: 400; }
  .clinic-title__main { display: block; font-size: 48px; font-weight: 700; margin-top: 2px; }

  .info-column {
    position: absolute; right: 40px; top: 35px; width: 310px;
    text-align: right; color: var(--ink); font-size: 10.6px; line-height: 15px;
    white-space: nowrap;
  }
  .info-column p { margin-bottom: 11px; }
  .highlight-cyan { color: var(--cyan); font-weight: 700; }
  .highlight-navy { color: var(--navy); font-weight: 700; }

  .signoff {
    border-top: 1px solid var(--rule); margin-left: 90px; padding-top: 8px;
    display: flex; justify-content: flex-end; align-items: center; gap: 8px;
  }
  .signoff__mark { width: 20px; height: 20px; border-radius: 50%; background: var(--navy); }
  .signoff__name { font-size: 15px; color: #222; font-weight: 400; line-height: 1.1; text-align: left; }

  .promise-badge {
    position: absolute; left: 212px; top: 150px; width: 156px; height: 156px;
    border-radius: 50%; background: var(--navy); color: var(--paper);
    display: flex; align-items: center; justify-content: center; text-align: center;
    font-size: 13px; font-weight: 700; line-height: 18px; white-space: nowrap;
  }

  .info-column--back { top: 42px; font-size: 10.2px; line-height: 14.3px; }
  .info-column--back p { margin-bottom: 10px; }
  .membership-note { color: var(--navy); margin-bottom: 5px !important; }
  .membership-badges { display: flex; justify-content: flex-end; align-items: center; gap: 10px; margin-bottom: 12px; }
  .badge-plain--wide { width: 84px; height: 26px; background: var(--cyan); border-radius: 3px; }
  .badge-plain--square { width: 36px; height: 34px; border: 2px solid var(--navy); background: #eef3fa; }
</style>
</head>
<body>

<section class="flyer-page flyer-page--front">
  <svg class="page-shapes" width="650" height="460" aria-hidden="true">
    <path d="M0 0 H445 C 385 80, 330 170, 190 185 C 110 193, 50 185, 0 172 Z" fill="var(--cyan)"/>
    <path d="M445 0 C 310 110, 290 340, 410 460" fill="none" stroke="var(--navy)" stroke-width="4"/>
  </svg>
  <svg class="page-illustration" width="650" height="460" role="img" aria-label="Line illustration of a woman's abdomen with two cupped hands">
    <defs>
      <linearGradient id="illoFront" x1="0" y1="0" x2="0" y2="1">
        <stop offset="0" stop-color="#cbeaf7"/><stop offset="1" stop-color="#f3fbfe"/>
      </linearGradient>
    </defs>
    <path d="M0 180 C 60 192, 130 197, 200 190 C 260 182, 300 175, 325 172 C 312 280, 330 380, 390 460 H0 Z" fill="url(#illoFront)"/>
  </svg>

  <h1 class="clinic-title">
    <span class="clinic-title__top">The Larkspur</span>
    <span class="clinic-title__main">Bay Clinic</span>
  </h1>

  <div class="info-column">
    <p>The Larkspur Bay Clinic is a new<br>company providing Dietetic services<br>for people with gastrointestinal<br>disorders. The main client base<br>would be people suffering from<br>Irritable Bowel Syndrome.</p>
    <p class="highlight-cyan">IBS is a collection of symptoms<br>which (will be individual to the suffer)<br>including constipation/diarrhoea/<br>abdominal pain or discomfort/bloating/<br>belching/flatulence/stomach gurgling/<br>reflux/nausea/urgency/incomplete<br>emptying/fatigue/headaches.</p>
    <p><span class="highlight-navy">IBS affects approx 30% of the population.</span><br>Previous treatments have generally been<br>ineffectual and include medication,<br>hypnotherapy, healthy eating.</p>
    <p>Recently it has been found that the FODMAP<br>diet (a diet low in fermentable Carbohydrates)<br>has been effective in 75% of sufferers.</p>
    <div class="signoff">
      <span class="signoff__mark"></span>
      <span class="signoff__name">The Larkspur<br>Bay Clinic</span>
    </div>
  </div>
</section>

<section class="flyer-page flyer-page--back">
  <svg class="page-shapes" width="650" height="460" aria-hidden="true">
    <path d="M0 0 H445 C 385 80, 330 170, 190 185 C 110 193, 50 185, 0 172 Z" fill="var(--cyan)"/>
    <path d="M445 0 C 310 110, 290 340, 410 460" fill="none" stroke="var(--navy)" stroke-width="4"/>
  </svg>
  <svg class="page-illustration" width="650" height="460" role="img" aria-label="Line illustration of a woman's abdomen with two cupped hands">
    <defs>
      <linearGradient id="illoBack" x1="0" y1="0" x2="0" y2="1">
        <stop offset="0" stop-color="#cbeaf7"/><stop offset="1" stop-color="#f3fbfe"/>
      </linearGradient>
    </defs>
    <path d="M0 180 C 60 192, 130 197, 200 190 C 260 182, 300 175, 325 172 C 312 280, 330 380, 390 460 H0 Z" fill="url(#illoBack)"/>
  </svg>

  <h1 class="clinic-title">
    <span class="clinic-title__top">The Larkspur</span>
    <span class="clinic-title__main">Bay Clinic</span>
  </h1>

  <div class="promise-badge">The Larkspur<br>Bay Clinic is<br>the only clinic<br>in the UK<br>offering dietetic<br>lead specialist<br>services.</div>

  <div class="info-column info-column--back">
    <p>The Low FODMAP diet is complex<br>and it is highly recommended that it is<br>undertaken only under the supervision of<br>a suitably qualified dietitian. Treatment<br>is available within the QWR but is usually<br>accessible only following consultation with<br>a Gastroenterologist. Most GP's have never<br>heard of this treatment as the research was<br>only published in 2009 in Australia and is yet to<br>filter through to the general practitioner.</p>
    <p class="membership-note">I am a member of the KSL and RWMT</p>
    <div class="membership-badges">
      <span class="badge-plain--wide"></span>
      <span class="badge-plain--square"></span>
    </div>
    <p>The flyer would be double sided, informing the<br>patient of all the self help steps they could take<br>if they have IBS then recommending that they<br>contact the Larkspur Bay clinic for specialist advice.</p>
    <p>Self Help: Healthy eating, regular meals, good<br>intake of non caffeinated non alcoholic non fizzy<br>drinks, regular exercise, stress management.</p>
    <p>The flyer would be left in GP surgeries,<br>Health centres, holistic therapy centres,<br>or through doors.</p>
  </div>
</section>

</body>
</html>
```